Website - Tides Of Bloom

We are catalysts of change in people's lives.
We work with individuals and professionals to bring about instant substantial & transforming change in their lives.
We provide one-on-one lifestyle coaching by an experienced practitioner.
Our existing website is www.tidesofbloom.biz & this site contains our the basis for the content of our desired new project, so please examine this carefully.
We require a professional and captivating website that will instantly impress, engage invite our readers to click & invest their lives.
Our services do not come cheap, but are second to none.
Our website must be contemporary whilst reflecting indisputable class & ultra-confidence in the success of our work.
Target Market(s)
Those who seek to want to change in their lives. Those aged primarily between 30 and 50 years of age, male or female.
Industry/Entity Type
Work
Look and feel

```html
<!DOCTYPE html>
<html lang="en">
<head>
<meta charset="utf-8">
<title>Tides Of Bloom</title>
<link rel="stylesheet" href="https://fonts.googleapis.com/css2?family=Montserrat:wght@300;400;700&family=Lato:ital,wght@0,400;0,700;1,400&display=swap">
<style>
:root{
  --black:#000;
  --ink:#1a1a1a;
  --white:#fff;
  --blue:#3aadd5;
  --red:#e0302e;
  --dark-left:#1f1f1f;
  --dark-right:#2b2b2b;
  --btn-left:#353535;
  --btn-right:#1b1b1b;
  --footer:#ececec;
  --grey-text:#555;
  --dot:#e86a6a;
  --dot-active:#d63b3b;
}
*{margin:0;padding:0;box-sizing:border-box}
html,body{width:806px;height:1200px;overflow:hidden}
body{font-family:"Lato",sans-serif;color:var(--ink);background:var(--white);position:relative}
.heading{font-family:"Montserrat",sans-serif}
.heading b{font-weight:700}
.heading span{font-weight:400}

.site-header{height:58px;background:var(--black);position:relative}
.brand{position:absolute;left:152px;top:12px;display:flex;align-items:center;gap:8px}
.brand-mark{width:32px;height:32px;border-radius:50%;background:var(--blue)}
.brand-name{font-family:"Lato",sans-serif;font-size:15px;font-weight:700;color:var(--white);line-height:1}
.main-nav{position:absolute;top:21px;left:444px;display:flex;font-size:8px;color:var(--white)}
.main-nav a{color:inherit;text-decoration:none;position:absolute;white-space:nowrap}
.main-nav .active::after{content:"";position:absolute;left:-7px;right:-7px;top:17px;height:1px;background:#777}

.hero{height:215px;position:relative;overflow:hidden}
.hero-photo{position:absolute;inset:0;background:radial-gradient(ellipse at 50% 20%,#7a7a7a 0%,#4b4b4b 45%,#2a2a2a 100%)}
.hero-content{position:absolute;left:0;right:0;top:66px;text-align:center;color:var(--white)}
.hero-title{font-size:30px;line-height:36px;letter-spacing:-.2px}
.hero-title span{font-weight:300}
.hero-text{width:480px;margin:12px auto 0;font-size:7.6px;line-height:9.4px}
.btn-outline{display:inline-block;margin-top:16px;width:98px;height:26px;line-height:22px;border:2px solid var(--white);font-size:8px;font-weight:700;color:var(--white)}

.features{height:205px;background:var(--blue);position:relative}
.feature{position:absolute;top:37px;width:118px;margin-left:-59px;text-align:center;color:var(--white)}
.feature-badge{width:72px;height:72px;margin:0 auto;border-radius:50%;background:var(--white);color:#333;display:flex;flex-direction:column;align-items:center;justify-content:center;gap:4px}
.feature-badge svg{width:22px;height:22px}
.feature-badge em{font-size:9px;font-style:italic}
.feature p{margin-top:15px;font-size:6.6px;font-weight:700;line-height:8.4px}
.feature a{display:block;margin-top:6px;font-size:6.8px;font-weight:700;color:var(--white);text-decoration:none}

.practitioners{height:259px;text-align:center;border-bottom:1px solid #e6e6e6}
.section-title{font-size:17px;padding-top:34px;color:var(--ink)}
.practitioners .lead{width:460px;margin:13px auto 0;font-size:8.4px;line-height:10.6px}
.help-row{position:absolute;top:594px;left:201px;display:flex;gap:20px}
.help-card{width:121px;height:99px;background:var(--red);color:var(--white);position:relative;padding-top:8px;font-family:"Montserrat",sans-serif;font-size:9px;line-height:12px}
.help-card::after{content:"";position:absolute;left:53px;bottom:-7px;border-left:7px solid transparent;border-right:7px solid transparent;border-top:7px solid var(--red)}
.help-card svg{width:38px;height:38px;display:block;margin:0 auto 8px}
.help-card b{font-weight:700}

.testimonials{height:137px;text-align:center;position:relative}
.testimonials .section-title{padding-top:26px}
.quote{width:460px;margin:10px auto 0;font-size:7.7px;line-height:9.6px;color:#333}
.quote-mark{position:absolute;font-family:"Montserrat",sans-serif;font-size:30px;color:#c8c8c8;line-height:1}
.dots{display:flex;gap:5px;justify-content:center;margin-top:13px}
.dots i{width:6px;height:6px;border-radius:50%;background:var(--dot)}
.dots i.on{background:var(--dot-active)}

.pillars{height:245px;display:flex;color:var(--white)}
.pillar{flex:1;padding:28px 0 0 151px;position:relative}
.pillar-left{background:var(--dark-left)}
.pillar-right{background:var(--dark-right);padding-left:30px}
.pillar h3{font-size:13px;line-height:16px}
.pillar h3::after{content:"";display:block;width:78px;height:1px;background:#555;margin-top:6px}
.pillar p{width:226px;font-size:7.2px;line-height:9px;margin-top:9px}
.pillar h3+p{margin-top:8px}
.btn-solid{position:absolute;top:202px;width:62px;height:23px;line-height:23px;text-align:center;font-size:7px;color:var(--white);text-decoration:none}
.pillar-left .btn-solid{background:var(--btn-left)}
.pillar-right .btn-solid{background:var(--btn-right)}

.site-footer{height:80px;background:var(--footer);text-align:center;padding-top:15px;font-size:7px;color:#222}
.social{display:flex;gap:7px;justify-content:center}
.social i{width:14px;height:14px;border-radius:50%;background:#333}
.footer-nav{display:flex;gap:26px;justify-content:center;margin-top:8px}
.footer-nav a{color:inherit;text-decoration:none}
.copyright{margin-top:9px;font-size:6.6px}
</style>
</head>
<body>

<header class="site-header">
  <div class="brand"><span class="brand-mark"></span><span class="brand-name">Tides Of Bloom</span></div>
  <nav class="main-nav">
    <a class="active" href="#" style="left:7px">Home</a>
    <a href="#" style="left:58px">Business</a>
    <a href="#" style="left:117px">Individuals</a>
    <a href="#" style="left:183px">Contact</a>
  </nav>
</header>

<section class="hero">
  <div class="hero-photo" role="img" aria-label="Black and white photo of a man seen from behind with arms outstretched against a cloudy sky"></div>
  <div class="hero-content">
    <h1 class="hero-title heading"><b>We Change Your</b> <span>Dimension of Life</span></h1>
    <p class="hero-text">Sed ut perspiciatis unde omnis iste natus error sit voluptatem accusantium doloremque laudantium, totam rem aperiam, eaque ipsa quae ab illo inventore veritatis et quasi architecto beatae vitae dicta sunt explicabo. Nemo enim ipsam voluptatem quia voluptas sit aspernatur aut odit aut fugit, sed quia consequuntur magni dolores eos qui ratione voluptatem sequi nesciunt.</p>
    <a class="btn-outline">Read More</a>
  </div>
</section>

<section class="features">
  <div class="feature" style="left:211px">
    <div class="feature-badge">
      <svg viewBox="0 0 24 24"><circle cx="12" cy="4" r="2.4" fill="#333"/><path d="M9 9h5l-2 11h2.5v2H8v-2h2l1.5-9H9z" fill="#333"/></svg>
      <em>About Us</em>
    </div>
    <p>Lorem ipsum dolor sit amet, consectetur adipisicing elit, sed do eiusmod tempor incididunt ut labore et commodo consequat.</p>
    <a>Read More</a>
  </div>
  <div class="feature" style="left:339px">
    <div class="feature-badge">
      <svg viewBox="0 0 24 24" fill="none" stroke="#333" stroke-width="2.2"><circle cx="12" cy="12" r="6.5"/><circle cx="12" cy="12" r="2" fill="#333"/><path d="M12 1v5M12 18v5M1 12h5M18 12h5"/></svg>
      <em>Our Aim</em>
    </div>
    <p>Lorem ipsum dolor sit amet, consectetur adipisicing elit, sed do eiusmod tempor incididunt ut labore et commodo consequat.</p>
    <a>Read More</a>
  </div>
  <div class="feature" style="left:468px">
    <div class="feature-badge">
      <svg viewBox="0 0 28 24" fill="#333" style="width:28px"><circle cx="6" cy="8" r="3"/><circle cx="22" cy="8" r="3"/><circle cx="14" cy="6.5" r="3.6"/><path d="M0 20c0-5 3-7 6-7s4 1 4 1v6zM28 20c0-5-3-7-6-7s-4 1-4 1v6zM8 21c0-6 3-9 6-9s6 3 6 9z"/></svg>
      <em>Our Team</em>
    </div>
    <p>Lorem ipsum dolor sit amet, consectetur adipisicing elit, sed do eiusmod tempor incididunt ut labore et commodo consequat.</p>
    <a>Read More</a>
  </div>
  <div class="feature" style="left:596px">
    <div class="feature-badge">
      <svg viewBox="0 0 24 24"><path d="M7 8a5 5 0 0 1 10 0c0 4-4 4-4 8h-3c0-5 4-5 4-8a2 2 0 0 0-4 0z" fill="#333"/><circle cx="11.5" cy="20.5" r="2" fill="#333"/></svg>
      <em>Quick Enquery</em>
    </div>
    <p>Lorem ipsum dolor sit amet, consectetur adipisicing elit, sed do eiusmod tempor incididunt ut labore et commodo consequat.</p>
    <a>Read More</a>
  </div>
</section>

<section class="practitioners">
  <h2 class="section-title heading"><b>What Our Practitioners</b> <span>Can Do For You ?</span></h2>
  <p class="lead">At Tides Of Bloom, our Master Practitioner will inspire you, shifting your perspective &amp; facilitating your mind with the freedom to realise your dreams.</p>
  <div class="help-row">
    <div class="help-card">
      <svg viewBox="0 0 40 40" fill="none" stroke="#fff" stroke-width="3"><circle cx="20" cy="20" r="16"/></svg>
      <b>We Help You To</b> Improve Your Behaviours And Emotions
    </div>
    <div class="help-card">
      <svg viewBox="0 0 40 40"><path d="M20 30C10 22 8 18 8 14a6 6 0 0 1 12-2 6 6 0 0 1 12 2c0 4-2 8-12 16z" fill="#fff"/><path d="M3 22c3 8 9 12 14 13M37 22c-3 8-9 12-14 13" stroke="#fff" stroke-width="2.5" fill="none"/></svg>
      <b>We Help You To</b> Improve Your relationships &amp; Communication
    </div>
    <div class="help-card">
      <svg viewBox="0 0 40 40"><path d="M20 4a11 11 0 0 0-6 20v5h12v-5a11 11 0 0 0-6-20z" fill="#fff"/><rect x="15" y="31" width="10" height="3" fill="#fff"/><rect x="16.5" y="35.5" width="7" height="2.5" fill="#fff"/></svg>
      <b>We Help You To</b> Become A Greater &amp; Broad Thinker
    </div>
  </div>
</section>

<section class="testimonials">
  <h2 class="section-title heading"><b>What Our Clients</b> <span>Say About Us ?</span></h2>
  <span class="quote-mark" style="left:150px;top:52px">&ldquo;</span>
  <p class="quote">Sed ut perspiciatis unde omnis iste natus error sit voluptatem accusantium doloremque laudantium, totam rem aperiam, eaque ipsa quae ab illo inventore veritatis et quasi architecto beatae vitae dicta sunt explicabo. Nemo enim ipsam voluptatem quia voluptas sit aspernatur aut odit aut fugit, sed quia consequuntur magni dolores eos qui ratione voluptatem sequi nesciunt.</p>
  <span class="quote-mark" style="left:601px;top:80px">&rdquo;</span>
  <div class="dots"><i></i><i></i><i class="on"></i><i></i><i></i></div>
</section>

<section class="pillars">
  <div class="pillar pillar-left">
    <h3 class="heading"><b>We Inspire Business</b> <span>Excellence</span></h3>
    <p>Tides Of Bloom have worked with CEO's &amp; business owners throughout Australia, as catalysts to their outstanding success.</p>
    <p>We will facilitate &amp; oversee your development of better and more effective ways of increasing performance and improving effectiveness.</p>
    <p>Imagine your professional life both consistent &amp; predictable. Your effectiveness with others dramatically increased, and having at your fingertips the ability to empower yourself for optimum results - any time you desire them.</p>
    <p>Generate potent, empowering emotional states within yourself at will, and eliminate negative and limiting emotions.</p>
    <a class="btn-solid">Read More</a>
  </div>
  <div class="pillar pillar-right">
    <h3 class="heading"><b>Individual Shift For</b> <span>Outstanding Life</span></h3>
    <p>Tides Of Bloom have worked with CEO's &amp; business owners throughout Australia, as catalysts to their outstanding success.</p>
    <p>We will facilitate &amp; oversee your development of better and more effective ways of increasing performance and improving effectiveness.</p>
    <p>Imagine your professional life both consistent &amp; predictable. Your effectiveness with others dramatically increased, and having at your fingertips the ability to empower yourself for optimum results - any time you desire them.</p>
    <p>Generate potent, empowering emotional states within yourself at will, and eliminate negative and limiting emotions.</p>
    <a class="btn-solid">Read More</a>
  </div>
</section>

<footer class="site-footer">
  <div class="social"><i></i><i></i><i></i></div>
  <nav class="footer-nav"><a>Home</a><a>Business</a><a>Individuals</a><a>Contact</a><a>Terms &amp; Conditions</a><a>Privacy Policy</a></nav>
  <p class="copyright">Copyright © 2013 Tides Of Bloom. All Rights Reserved.</p>
</footer>

</body>
</html>
```